Create magical pull-up signs for The Velvet Paw House!

We need two pull-up signs that will be used for expos and conventions. Each sign will be for a different part of our business, so the design will be the same, although the colours, photos and text will be different.

Each sign will be 850x2000mm (see attached design guide).

The first sign is for The Velvet Paw House Pet Resort, and will be purple and teal (see attached logo).
It needs to have the following bullet points:
"Conveniently Located at Kestrel Field Terminal
Fully Air-Conditioned Dog & Cat Suites
Experienced & Loving Godparents
Purpose Built & Designed Especially for your Furkid
Full Interstate Pet Travel Agency & Pet Taxi"
It also needs to have the following contact info:
Ph: 1300 7 PLUMS (1300 7 75867)
www.plumpaw.com.au
stay@plumpaw.com.au
facebook.com/plumpawlodge (can use the Facebook logo instead of facebook.com)
Photos for this sign can be found at https://pixvault.example/album/Qm3rTzLw8Hk2Np

The second sign is for The Velvet Paw House Doggy Daycare, and will be red and blue (see attached logo).
"You Work, They Play!
Indoor & Outdoor Play Areas
Two Convenient Locations- Winnellie & Kestrel Field Terminal"
www.plumpaw.com.au
play@plumpaw.com.au
facebook.com/plumpawplay (can use the Facebook logo instead of facebook.com)
Photos for this sign can be found at https://pixvault.example/album/Zv7bXsRe4Jd9Cy

Industry/Entity Type

Business

Font styles to use
Sans Serif

Requirements
Must have
• Please emphasise the text and photos over the contact information. These stands need to be eye catching and appealing to people walking past in order to bring them to our expo stands.

```html
<!DOCTYPE html>
<html lang="en">
<head>
<meta charset="utf-8">
<title>The Velvet Paw House Pet Resort – Pull-up Banner</title>
<link href="https://fonts.googleapis.com/css2?family=Encode+Sans+Semi+Condensed:wght@400;600&display=swap" rel="stylesheet">
<style>
  :root{
    --stage:#c9c9c9;
    --paper:#f3f3f3;
    --teal:#1fb9ad;
    --teal-dark:#139488;
    --purple:#a42a9e;
    --purple-deep:#8a1f88;
    --ink:#2b2b2b;
    --white:#ffffff;
  }
  *{box-sizing:border-box;margin:0;padding:0}
  html,body{width:1200px;height:1200px;overflow:hidden;background:var(--stage);
    font-family:"Encode Sans Semi Condensed",Arial,sans-serif;color:var(--ink)}
  .banner{position:absolute;left:360px;top:35px;width:480px;height:1130px;
    background:var(--paper);overflow:hidden;box-shadow:0 6px 18px rgba(0,0,0,.18)}
  .banner-bg{position:absolute;inset:0}
  .feature-circle{position:absolute;width:150px;height:150px;border-radius:50%;
    border:7px solid var(--teal);overflow:hidden;box-shadow:0 0 0 3px var(--paper)}
  .feature-circle--one{left:90px;top:278px;background:radial-gradient(circle at 50% 40%,#d6a57a,#b9824f 45%,#5f8a3e 100%)}
  .feature-circle--two{left:255px;top:278px;background:radial-gradient(circle at 50% 55%,#8fd3e3,#a8764c 55%,#3e3e3e 100%)}
  .brand{position:absolute;left:0;right:0;top:462px;text-align:center}
  .brand-mark{display:block;width:38px;height:38px;border-radius:50%;background:var(--purple);margin:0 auto 8px}
  .brand-name{font-size:21px;font-weight:600;color:var(--teal-dark);line-height:1.1}
  .features{position:absolute;left:0;top:602px;width:480px;height:300px}
  .feature{position:absolute;width:170px;text-align:center;transform:translateX(-50%)}
  .feature-icon{width:62px;height:62px;border-radius:50%;margin:0 auto 12px;
    background:var(--teal);border:3px solid var(--purple);display:flex;align-items:center;justify-content:center}
  .feature-icon svg{width:34px;height:34px}
  .feature-text{font-size:14.5px;line-height:1.3;color:var(--ink)}
  .contact{position:absolute;left:0;right:0;top:1040px;display:flex;align-items:center;
    padding:0 26px;color:var(--white);font-size:14px}
  .contact-group{display:flex;flex-direction:column;gap:6px}
  .contact-line{display:flex;align-items:center;gap:7px}
  .contact-dot{width:12px;height:12px;border-radius:50%;background:var(--teal);flex:none;display:flex;align-items:center;justify-content:center}
  .contact-divider{width:2px;height:46px;background:var(--white);margin:0 20px 0 50px}
</style>
</head>
<body>
<main class="banner">
  <svg class="banner-bg" viewBox="0 0 480 1130" width="480" height="1130">
    <defs>
      <linearGradient id="heroTone" x1="0" y1="0" x2="0.35" y2="1">
        <stop offset="0" stop-color="#8d949b"/>
        <stop offset=".3" stop-color="#b7aca4"/>
        <stop offset=".55" stop-color="#d8b9a2"/>
        <stop offset=".8" stop-color="#a9a3ad"/>
        <stop offset="1" stop-color="#8f86b3"/>
      </linearGradient>
      <linearGradient id="footTone" x1="0" y1="0" x2="1" y2="1">
        <stop offset="0" stop-color="#8f1f8d"/>
        <stop offset=".6" stop-color="#b032ab"/>
        <stop offset="1" stop-color="#9a2497"/>
      </linearGradient>
    </defs>
    <path role="img" aria-label="Photo of a smiling girl cuddling a spotted dog in a kennel run"
      d="M0 0 H480 V372 Q470 405 430 410 L150 420 Q95 422 78 440 L58 454 Q30 395 0 330 Z" fill="url(#heroTone)"/>
    <path d="M0 330 Q30 395 58 454 L78 440 Q95 422 150 420 L430 410 Q470 405 480 372"
      fill="none" stroke="var(--teal)" stroke-width="7" stroke-linejoin="round"/>
    <path d="M330 438 Q420 425 455 410 Q475 400 480 392" fill="none" stroke="var(--purple)" stroke-width="6" stroke-linecap="round"/>
    <path d="M0 1130 V1040 Q20 985 120 975 Q250 962 330 945 Q345 940 355 920 Q370 955 420 975 Q465 990 480 1010 V1130 Z" fill="url(#footTone)"/>
    <path d="M0 1040 Q20 985 120 975 Q250 962 330 945 Q345 940 355 920 Q370 955 420 975 Q465 990 480 1010" fill="none" stroke="var(--teal)" stroke-width="6"/>
  </svg>

  <div class="feature-circle feature-circle--one" role="img" aria-label="Photo of a happy tan and white dog on grass"></div>
  <div class="feature-circle feature-circle--two" role="img" aria-label="Photo of dogs drinking from a blue water fountain"></div>

  <header class="brand">
    <span class="brand-mark"></span>
    <h1 class="brand-name">The Velvet Paw House<br>Pet Resort</h1>
  </header>

  <section class="features">
    <div class="feature" style="left:165px;top:0">
      <span class="feature-icon"><svg viewBox="0 0 24 24"><path fill="#fff" d="M21 16v-2l-8-5V3.5a1.5 1.5 0 0 0-3 0V9l-8 5v2l8-2.5V19l-2 1.5V22l3.5-1 3.5 1v-1.5L13 19v-5.5z"/></svg></span>
      <p class="feature-text">Conveniently Located<br>at Kestrel Field Terminal</p>
    </div>
    <div class="feature" style="left:329px;top:-6px">
      <span class="feature-icon" role="img" aria-label="Dog silhouette icon"></span>
      <p class="feature-text">Fully Air-Conditioned<br>Dog &amp; Cat Suites</p>
    </div>
    <div class="feature" style="left:95px;top:148px">
      <span class="feature-icon"><svg viewBox="0 0 24 24"><path fill="none" stroke="#fff" stroke-width="3.4" stroke-linecap="round" stroke-linejoin="round" d="M4 12.5l5 5L20 6"/></svg></span>
      <p class="feature-text">Experienced<br>and Loving<br>Godparents</p>
    </div>
    <div class="feature" style="left:243px;top:145px">
      <span class="feature-icon"><svg viewBox="0 0 24 24"><g fill="none" stroke="#fff" stroke-width="1.8"><path d="M8 16l8-8"/><circle cx="6" cy="15.5" r="2.2"/><circle cx="8.5" cy="18" r="2.2"/><circle cx="15.5" cy="6" r="2.2"/><circle cx="18" cy="8.5" r="2.2"/></g></svg></span>
      <p class="feature-text">Purpose Built<br>&amp; Designed Especially<br>for your Furkid</p>
    </div>
    <div class="feature" style="left:385px;top:136px">
      <span class="feature-icon"><svg viewBox="0 0 24 24"><path fill="#fff" d="M10 3h4v2h2.5l2 5H20a1 1 0 0 1 1 1v6h-2v2h-3v-2H8v2H5v-2H3v-6a1 1 0 0 1 1-1h1.5l2-5H10zM8.5 7 7 10h10l-1.5-3zM6.5 12.5a1.3 1.3 0 1 0 0 2.6 1.3 1.3 0 0 0 0-2.6zm11 0a1.3 1.3 0 1 0 0 2.6 1.3 1.3 0 0 0 0-2.6z"/></svg></span>
      <p class="feature-text">Full Interstate Pet<br>Travel Agency<br>&amp; Pet Taxi</p>
    </div>
  </section>

  <footer class="contact">
    <div class="contact-group">
      <span class="contact-line"><span class="contact-dot"><svg viewBox="0 0 24 24" width="8" height="8"><path fill="#fff" d="M6.6 10.8a15 15 0 0 0 6.6 6.6l2.2-2.2a1 1 0 0 1 1-.25 11 11 0 0 0 3.6.6 1 1 0 0 1 1 1V20a1 1 0 0 1-1 1A17 17 0 0 1 3 4a1 1 0 0 1 1-1h3.5a1 1 0 0 1 1 1 11 11 0 0 0 .6 3.6 1 1 0 0 1-.25 1z"/></svg></span>1300 7 PLUMS (1300 7 75867)</span>
      <span class="contact-line"><span class="contact-dot"></span>Visit: www.plumpaw.com.au</span>
    </div>
    <span class="contact-divider"></span>
    <div class="contact-group">
      <span class="contact-line"><span class="contact-dot"></span>stay@plumpaw.com.au</span>
      <span class="contact-line"><span class="contact-dot"></span>plumpawlodge</span>
    </div>
  </footer>
</main>
</body>
</html>
```